Real Estate Business Cards

Looking for a clean, sharp and professional look for our Real Estate investment Fund that invests in Multi Family Apartment buildings.

Target Market(s)

Real Estate Fund

Industry/Entity Type

Real Estate

Contact Information for Business Card

Company Description: Real Estate Investment Fund
Company Name: KRV Holdings
Name: Marcus Tovell
Cell: (917) 482-0957
Email: marcus@krvholdings-example.com
Website: www.krvholdings-example.com
Address: 148, 7th Street, Brooklyn NY 11217

Colors

Designer to choose colors to be used in the design.

Requirements
Nice to have
• Colors to match logo

```html
<!DOCTYPE html>
<html lang="en">
<head>
<meta charset="utf-8">
<title>KRV Holdings — Business Cards</title>
<link rel="stylesheet" href="https://fonts.googleapis.com/css2?family=Cinzel:wght@400;500&family=Poppins:wght@300;400&display=swap">
<style>
  :root {
    --fund-blue: #0f6aa6;
    --slate: #3d3f43;
    --paper: #ffffff;
    --backdrop: #dcdddf;
    --ink-soft: #4a4c50;
  }
  * { box-sizing: border-box; margin: 0; padding: 0; }
  html, body { width: 1200px; height: 801px; overflow: hidden; }
  body {
    background: var(--backdrop);
    display: flex;
    align-items: center;
    justify-content: center;
    gap: 44px;
    font-family: "Poppins", sans-serif;
  }
  .card {
    position: relative;
    width: 520px;
    height: 297px;
    background: var(--paper);
    overflow: hidden;
  }

  /* Front side */
  .card-front .blue-field {
    position: absolute;
    inset: 0;
    background: var(--fund-blue);
    clip-path: polygon(0 0, 58% 0, 100% 100%, 0 100%);
  }
  .card-front .diagonal-rule {
    position: absolute;
    inset: 0;
    background: var(--slate);
    clip-path: polygon(58% 0, 63% 0, 100% 92%, 100% 100%);
  }
  .front-content {
    position: absolute;
    left: 34px;
    top: 34px;
    color: var(--paper);
  }
  .front-company {
    font-family: "Cinzel", serif;
    font-size: 23px;
    font-weight: 400;
    letter-spacing: 0.5px;
    text-transform: uppercase;
  }
  .front-person {
    margin-top: 62px;
    font-family: "Cinzel", serif;
    font-size: 19px;
    letter-spacing: 0.5px;
    text-transform: uppercase;
  }
  .address {
    margin-top: 8px;
    font-size: 12px;
    line-height: 1.35;
    font-weight: 300;
  }
  .contact-list {
    list-style: none;
    margin-top: 10px;
    font-size: 12px;
    line-height: 1.45;
    font-weight: 300;
  }
  .contact-list li { display: flex; align-items: center; gap: 7px; }
  .contact-list svg { width: 10px; height: 10px; flex: none; }

  /* Back side */
  .card-back .brand-lockup {
    position: absolute;
    left: 70px;
    top: 96px;
    display: flex;
    align-items: center;
    gap: 16px;
  }
  .brand-square {
    width: 46px;
    height: 46px;
    background: var(--fund-blue);
  }
  .back-company {
    font-family: "Cinzel", serif;
    font-size: 34px;
    font-weight: 400;
    color: var(--fund-blue);
    text-transform: uppercase;
    letter-spacing: 0.5px;
  }
  .back-domain {
    position: absolute;
    left: 132px;
    top: 150px;
    font-size: 11px;
    letter-spacing: 5px;
    color: var(--ink-soft);
  }
  .back-web {
    position: absolute;
    left: 0;
    right: 0;
    bottom: 52px;
    text-align: center;
    font-size: 12px;
    letter-spacing: 5px;
    color: var(--ink-soft);
  }
  .back-web .web-name { color: var(--fund-blue); }
</style>
</head>
<body>

  <section class="card card-front" aria-label="Business card front">
    <div class="blue-field"></div>
    <div class="diagonal-rule"></div>
    <div class="front-content">
      <h1 class="front-company">KRV Holdings</h1>
      <h2 class="front-person">Marcus Tovell</h2>
      <p class="address">148, 7th Street<br>Brooklyn NY 11217</p>
      <ul class="contact-list">
        <li>
          <svg viewBox="0 0 10 10"><rect x="2" y="0.5" width="6" height="9" rx="1" fill="none" stroke="#fff" stroke-width="1.2"/></svg>
          (917) 482-0957
        </li>
        <li>
          <svg viewBox="0 0 10 10"><rect x="0.5" y="2" width="9" height="6.5" fill="none" stroke="#fff" stroke-width="1.1"/><path d="M0.5 2 L5 5.5 L9.5 2" fill="none" stroke="#fff" stroke-width="1.1"/></svg>
          marcus@krvholdings-example.com
        </li>
        <li>
          <svg viewBox="0 0 10 10"><circle cx="5" cy="5" r="4.3" fill="none" stroke="#fff" stroke-width="1.1"/><path d="M0.7 5 H9.3 M5 0.7 C2.5 3 2.5 7 5 9.3 M5 0.7 C7.5 3 7.5 7 5 9.3" fill="none" stroke="#fff" stroke-width="0.9"/></svg>
          www.krvholdings-example.com
        </li>
      </ul>
    </div>
  </section>

  <section class="card card-back" aria-label="Business card back">
    <div class="brand-lockup">
      <div class="brand-square"></div>
      <h2 class="back-company">KRV Holdings</h2>
    </div>
    <p class="back-domain">krvholdings-example.com</p>
    <p class="back-web">www.<span class="web-name">krvholdings-example</span>.com</p>
  </section>

</body>
</html>
```